Harlow Crest Holdings (Remodeling company) needs a logo and business card

We need a business card design for a new company. We "flip" upmarket houses (buy, remodel and sell) in the Austin, TX area. I'd like neutral colors (grey, white, gold black). I would like it to include a simple, clean logo. Our designs are modern and uncluttered and I would like that reflected in the business card design.

Target Market(s)

Young professionals, Families, Retirees. Our properties will sell for $750k+

Industry/Entity Type

Real Estate

Contact Information for Business Card

Harlow Crets Holdings
Mona Harlow
(979) 555 0142
Owner
Rolf Tandem
(512) 555 0176
Realtor

Logo Text

Harlow Crest Holdings

Font styles to use
Serif
Script

Requirements
Must have
• Simple, classic design
Nice to have
• Clean lines, modern look
Should not have
• Too traditionally

```html
<!DOCTYPE html>
<html lang="en">
<head>
<meta charset="utf-8">
<title>Harlow Crest Holdings — Business Cards</title>
<link href="https://fonts.googleapis.com/css2?family=Playfair+Display:wght@700;900&family=Josefin+Sans:wght@400;600&display=swap" rel="stylesheet">
<style>
  :root {
    --page: #ffffff;
    --card-dark: #111111;
    --card-mid: #1c1c1c;
    --gold: #e2b13c;
    --gold-light: #f6d77a;
    --gold-deep: #b9791d;
    --pattern-bg: #141414;
  }
  html, body {
    margin: 0;
    padding: 0;
    width: 1200px;
    height: 1200px;
    overflow: hidden;
    background: var(--page);
  }
  .canvas {
    position: relative;
    width: 1200px;
    height: 1200px;
  }
  .card {
    position: absolute;
    left: 201px;
    width: 779px;
    height: 444px;
    background: radial-gradient(ellipse at 35% 40%, var(--card-mid), var(--card-dark) 75%);
    overflow: hidden;
  }
  .card--owner { top: 50px; }
  .card--realtor { top: 622px; }

  .card__pattern {
    position: absolute;
    left: 421px;
    top: 0;
    width: 358px;
    height: 100%;
    background:
      radial-gradient(circle at 75% 15%, rgba(246,215,122,0.55), transparent 40%),
      radial-gradient(circle at 30% 80%, rgba(226,177,60,0.5), transparent 45%),
      radial-gradient(circle at 50% 45%, rgba(20,20,20,0.8), transparent 60%),
      linear-gradient(135deg, var(--gold-deep), var(--pattern-bg) 45%, var(--gold) 100%);
  }

  .brand {
    position: absolute;
    left: 64px;
    top: 60px;
    display: flex;
    align-items: flex-end;
    gap: 10px;
  }
  .brand__mark {
    width: 24px;
    height: 24px;
    background: var(--gold);
    margin-bottom: 4px;
  }
  .brand__name {
    font-family: "Playfair Display", serif;
    font-weight: 700;
    font-size: 17px;
    line-height: 21px;
    letter-spacing: 0.3px;
    color: var(--gold);
    text-transform: uppercase;
  }
  .brand__line { display: block; }

  .person {
    position: absolute;
    left: 63px;
    top: 236px;
  }
  .person__name {
    margin: 0;
    font-family: "Playfair Display", serif;
    font-weight: 900;
    font-size: 44px;
    line-height: 1;
    background: linear-gradient(180deg, var(--gold-light), var(--gold) 55%, var(--gold-deep));
    -webkit-background-clip: text;
    background-clip: text;
    color: transparent;
  }
  .person__role {
    margin: 4px 0 0;
    font-family: "Playfair Display", serif;
    font-weight: 900;
    font-size: 20px;
    line-height: 1.1;
    color: var(--gold);
  }

  .contact {
    position: absolute;
    left: 62px;
    top: 331px;
    margin: 0;
    padding: 0;
    list-style: none;
    font-family: "Josefin Sans", sans-serif;
    font-weight: 600;
    font-size: 18px;
    color: var(--gold);
  }
  .contact__item {
    display: flex;
    align-items: center;
    gap: 18px;
    height: 26px;
    margin-bottom: 22px;
    white-space: nowrap;
  }
  .contact__icon {
    width: 20px;
    height: 20px;
    fill: var(--gold);
    flex: none;
  }
</style>
</head>
<body>
<main class="canvas">

  <section class="card card--owner">
    <div class="brand">
      <span class="brand__mark"></span>
      <span class="brand__name"><span class="brand__line">Harlow</span><span class="brand__line">Crets Holdings</span></span>
    </div>
    <div class="person">
      <h1 class="person__name">Mona Harlow</h1>
      <p class="person__role">Owner</p>
    </div>
    <ul class="contact">
      <li class="contact__item">
        <svg class="contact__icon" viewBox="0 0 24 24" aria-hidden="true"><path d="M6.6 10.8a15.1 15.1 0 0 0 6.6 6.6l2.2-2.2a1 1 0 0 1 1-.25 11.4 11.4 0 0 0 3.6.57 1 1 0 0 1 1 1V20a1 1 0 0 1-1 1A17 17 0 0 1 3 4a1 1 0 0 1 1-1h3.5a1 1 0 0 1 1 1c0 1.25.2 2.450.57 3.57a1 1 0 0 1-.25 1z"/></svg>
        <span>(979) 555 0142</span>
      </li>
      <li class="contact__item">
        <svg class="contact__icon" viewBox="0 0 24 24" aria-hidden="true"><path d="M12 2a7 7 0 0 0-7 7c0 5.2 7 13 7 13s7-7.8 7-13a7 7 0 0 0-7-7zm0 9.5A2.5 2.5 0 1 1 12 6.5a2.5 2.5 0 0 1 0 5z"/></svg>
        <span>Brookvale, TX Area, USA</span>
      </li>
    </ul>
    <div class="card__pattern" role="img" aria-label="Ornamental gold floral swirl pattern on black"></div>
  </section>

  <section class="card card--realtor">
    <div class="brand">
      <span class="brand__mark"></span>
      <span class="brand__name"><span class="brand__line">Harlow</span><span class="brand__line">Crets Holdings</span></span>
    </div>
    <div class="person">
      <h1 class="person__name">Rolf Tandem</h1>
      <p class="person__role">Realtor</p>
    </div>
    <ul class="contact">
      <li class="contact__item">
        <svg class="contact__icon" viewBox="0 0 24 24" aria-hidden="true"><path d="M6.6 10.8a15.1 15.1 0 0 0 6.6 6.6l2.2-2.2a1 1 0 0 1 1-.25 11.4 11.4 0 0 0 3.6.57 1 1 0 0 1 1 1V20a1 1 0 0 1-1 1A17 17 0 0 1 3 4a1 1 0 0 1 1-1h3.5a1 1 0 0 1 1 1c0 1.25.2 2.450.57 3.57a1 1 0 0 1-.25 1z"/></svg>
        <span>(512) 555 0176</span>
      </li>
      <li class="contact__item">
        <svg class="contact__icon" viewBox="0 0 24 24" aria-hidden="true"><path d="M12 2a7 7 0 0 0-7 7c0 5.2 7 13 7 13s7-7.8 7-13a7 7 0 0 0-7-7zm0 9.5A2.5 2.5 0 1 1 12 6.5a2.5 2.5 0 0 1 0 5z"/></svg>
        <span>Brookvale, TX Area, USA</span>
      </li>
    </ul>
    <div class="card__pattern" role="img" aria-label="Ornamental gold floral swirl pattern on black"></div>
  </section>

</main>
</body>
</html>
```